Real Estate "For Sale" Sign for construction company

We need a sign that we can use to hang on a post and place on the road when we sell a property. The sign will be simple and will need to mainly feature our logo (files attached), as well as the words "For Sale", and then our phone number "(555) 617 3489". The sign will hang on a post that'll look something like the attached picture.

Target Market(s)

Home buyers

Industry/Entity Type

Real Estate

Font styles to use
Serif
Sans Serif

Colors
0054AA
0677BA
7BADD7
CADEEF
E8F1F8
0094D4
00A9DD
6FCCEA
C7EBF8
E9F6FB

Requirements
Must have
• For Sale & our phone number

```html
<!DOCTYPE html>
<html lang="en">
<head>
<meta charset="UTF-8">
<title>For Sale Sign – Highland Ridge Properties</title>
<link href="https://fonts.googleapis.com/css2?family=Barlow+Condensed:wght@800&family=Oswald:wght@600&family=Montserrat:wght@500;700;800&display=swap" rel="stylesheet">
<style>
  :root {
    --navy: #0d3f94;
    --brand-blue: #0677ba;
    --band: #c7e5f8;
    --white: #ffffff;
    --backdrop: #eef1f4;
  }
  * { margin: 0; padding: 0; box-sizing: border-box; }
  html, body {
    width: 1200px;
    height: 1010px;
    overflow: hidden;
    background: var(--backdrop);
  }
  body { position: relative; }
  .sign {
    position: absolute;
    left: 240px;
    top: 25px;
    width: 720px;
    height: 960px;
    overflow: hidden;
    background: var(--white);
    box-shadow: 0 4px 18px rgba(0,0,0,0.12);
  }
  .headline {
    position: absolute;
    left: 62px;
    top: 0;
    font-family: "Barlow Condensed", "Arial Narrow", sans-serif;
    font-weight: 800;
    color: var(--navy);
    font-size: 310px;
    line-height: 232px;
    white-space: nowrap;
  }
  .headline span {
    display: block;
    height: 232px;
  }
  .contact-band {
    position: absolute;
    left: 0;
    top: 573px;
    width: 100%;
    height: 322px;
    background: var(--band);
  }
  .brand-mark {
    position: absolute;
    left: 50%;
    top: 522px;
    transform: translateX(-50%);
  }
  .brand-name {
    position: absolute;
    top: 644px;
    width: 100%;
    text-align: center;
    font-family: "Montserrat", sans-serif;
    font-weight: 500;
    color: var(--brand-blue);
    font-size: 38px;
    line-height: 48px;
    white-space: nowrap;
  }
  .call-line {
    position: absolute;
    top: 738px;
    width: 100%;
    height: 34px;
    display: flex;
    justify-content: center;
    align-items: center;
    gap: 14px;
    font-family: "Montserrat", sans-serif;
    font-weight: 800;
    font-size: 26px;
    color: var(--navy);
    white-space: nowrap;
  }
  .rule {
    display: inline-block;
    height: 3px;
    background: var(--navy);
  }
  .call-line .rule { width: 36px; }
  .phone {
    position: absolute;
    top: 768px;
    width: 100%;
    text-align: center;
    font-family: "Oswald", sans-serif;
    font-weight: 600;
    font-size: 110px;
    line-height: 116px;
    letter-spacing: -1px;
    white-space: nowrap;
    color: var(--navy);
  }
  .website {
    position: absolute;
    top: 895px;
    width: 100%;
    height: 65px;
    display: flex;
    justify-content: center;
    align-items: center;
    gap: 14px;
    font-family: "Montserrat", sans-serif;
    font-weight: 500;
    font-size: 27px;
    white-space: nowrap;
    color: var(--navy);
  }
  .website strong { font-weight: 700; }
  .website .rule { width: 54px; }
</style>
</head>
<body>
  <main class="sign">
    <h1 class="headline"><span>FOR</span><span>SALE</span></h1>
    <section class="contact-band"></section>
    <svg class="brand-mark" width="112" height="112" viewBox="0 0 112 112" aria-hidden="true">
      <circle cx="56" cy="56" r="54" fill="var(--brand-blue)"/>
    </svg>
    <p class="brand-name">Highland Ridge Properties</p>
    <p class="call-line"><span class="rule"></span>CALL OR TEXT ME AT<span class="rule"></span></p>
    <p class="phone">(555) 617 3489</p>
    <p class="website"><span class="rule"></span><span>www.<strong>highlandridge</strong>.com</span><span class="rule"></span></p>
  </main>
</body>
</html>
```